New Business Card Design Project

double sided business cards. i would like to design a business card with the logo attached . that logo being centered on 1 side and then my info on the other.

Wesley Brandt CEO
Phone# 334-617-2054
Wesley@fairoakhomecare.example

Contact Information for Business Card

double sided one side the Logo attached below that saying Home Maintenance and Repair Specialists then on back my info Wesley Brandt CEO Home Maintenance Specialist Phone# 334-617-2054 Wesley@fairoakhomecare.example

Font styles to use
Serif

Colors
0054AA
0677BA
7BADD7
CADEEF
E8F1F8
FFC000
F8CF3A
FAE287
FDF2CF
FEFAEE

Requirements
Must have
• double sided logo attached on one side with colors blue and gold. black background info on the other side

```html
<!DOCTYPE html>
<html lang="en">
<head>
<meta charset="utf-8">
<title>Fair Oak Home Care – Business Card</title>
<link href="https://fonts.googleapis.com/css2?family=Open+Sans:wght@400;600;700;800&display=swap" rel="stylesheet">
<style>
  :root {
    --backdrop: #d9d9d9;
    --card-dark: #262626;
    --card-dark-edge: #1c1c1c;
    --brand-blue: #1f74c9;
    --brand-gold: #e3b921;
    --gold-light: #ecd27c;
    --gold-mid: #d8b75a;
    --gold-deep: #c9a54a;
    --ink: #111111;
    --pattern-dark: #333333;
    --pattern-gold: #f3dc8c;
  }

  * { box-sizing: border-box; margin: 0; padding: 0; }

  html, body {
    width: 1200px;
    height: 846px;
    overflow: hidden;
    background: var(--backdrop);
    font-family: "Open Sans", Arial, sans-serif;
  }

  .canvas {
    position: relative;
    width: 1200px;
    height: 846px;
    display: flex;
    align-items: center;
    justify-content: center;
    gap: 60px;
  }

  .card {
    position: relative;
    width: 510px;
    height: 292px;
    border-radius: 4px;
    overflow: hidden;
    box-shadow: 0 14px 30px rgba(0,0,0,0.22);
  }

  /* ---------- Front ---------- */
  .card--front {
    background: linear-gradient(135deg, var(--card-dark) 0%, var(--card-dark-edge) 100%);
  }

  .card--front .pattern-area {
    position: absolute;
    left: 0;
    bottom: 0;
    width: 300px;
    height: 170px;
    background: linear-gradient(20deg, var(--pattern-dark) 0%, rgba(51,51,51,0) 75%);
  }

  .front-content {
    position: absolute;
    inset: 0;
    display: flex;
    flex-direction: column;
    align-items: center;
    justify-content: center;
    gap: 22px;
  }

  .brand {
    display: flex;
    align-items: center;
    gap: 12px;
  }

  .brand__mark {
    width: 20px;
    height: 20px;
  }

  .brand__name {
    font-weight: 700;
    font-size: 30px;
    letter-spacing: 1px;
    text-transform: uppercase;
    line-height: 1;
  }

  .card--front .brand__mark { background: var(--brand-gold); }
  .card--front .brand__name { color: var(--brand-blue); }

  .tagline {
    color: var(--brand-gold);
    font-weight: 700;
    font-size: 17px;
    letter-spacing: 0.2px;
  }

  /* ---------- Back ---------- */
  .card--back {
    background: linear-gradient(160deg, var(--gold-deep) 0%, var(--gold-mid) 45%, var(--gold-light) 100%);
  }

  .card--back .pattern-area {
    position: absolute;
    right: 0;
    top: 0;
    width: 260px;
    height: 292px;
    background: linear-gradient(225deg, var(--pattern-gold) 0%, rgba(243,220,140,0) 70%);
    opacity: 0.55;
  }

  .back-content {
    position: absolute;
    left: 44px;
    top: 50px;
    display: flex;
    flex-direction: column;
    gap: 26px;
  }

  .card--back .brand__mark { background: var(--ink); }
  .card--back .brand__name { color: var(--ink); font-size: 26px; }

  .contact {
    color: var(--ink);
    display: flex;
    flex-direction: column;
    gap: 8px;
  }

  .contact__name {
    font-size: 22px;
    font-weight: 800;
    line-height: 1.1;
  }

  .contact__role {
    font-weight: 400;
    font-size: 17px;
  }

  .contact__line {
    display: flex;
    align-items: center;
    gap: 10px;
    font-size: 15px;
  }

  .contact__icon {
    width: 18px;
    height: 18px;
    flex: none;
  }
</style>
</head>
<body>
  <main class="canvas">

    <section class="card card--front" aria-label="Card front">
      <div class="pattern-area" role="img" aria-label="Faint nested chevron line pattern"></div>
      <div class="front-content">
        <div class="brand">
          <span class="brand__mark"></span>
          <span class="brand__name">Fair Oak Home Care</span>
        </div>
        <p class="tagline">Home Maintenance and Repair Specialists</p>
      </div>
    </section>

    <section class="card card--back" aria-label="Card back">
      <div class="pattern-area" role="img" aria-label="Light gold nested chevron line pattern"></div>
      <div class="back-content">
        <div class="brand">
          <span class="brand__mark"></span>
          <span class="brand__name">Fair Oak Home Care</span>
        </div>
        <div class="contact">
          <p class="contact__name">Wesley Brandt <span class="contact__role">(CEO)</span></p>
          <p class="contact__line">
            <svg class="contact__icon" viewBox="0 0 18 18" aria-hidden="true">
              <rect width="18" height="18" rx="3" fill="#111"/>
              <path d="M6 4.5h2l1 3-1.4 1a6 6 0 0 0 2.9 2.9l1-1.4 3 1v2c0 .6-.5 1-1 1A9.5 9.5 0 0 1 5 5.5c0-.5.4-1 1-1z" fill="#e6c867" transform="translate(-1 -0.5) scale(0.95)"/>
            </svg>
            334-617-2054
          </p>
          <p class="contact__line">
            <svg class="contact__icon" viewBox="0 0 18 18" aria-hidden="true">
              <rect width="18" height="18" rx="3" fill="#111"/>
              <rect x="4" y="5.5" width="10" height="7" fill="none" stroke="#e6c867" stroke-width="1.3"/>
              <path d="M4 5.5l5 4 5-4" fill="none" stroke="#e6c867" stroke-width="1.3"/>
            </svg>
            Wesley@fairoakhomecare.example
          </p>
        </div>
      </div>
    </section>

  </main>
</body>
</html>
```